Flyer-Design für Anbieter von hochwertigem Futter für Kaninchen
Zielgruppe
Wir bieten hochwertiges Futter (Hauptfutter wie Heu aus eigener Herstellung aber auch Zusatzfutter) für Kaninchen.
Unsere Zielgruppe sind laut Auswertung unsers Online-Shops hauptsächlich weibliche Kunden (82%) und im Durchschnitt 40 Jahre alt.
Aufgabenstellung
Allgemeines:
- Flyer soll als Werbemedium gestaltet werden
- Design im Querformat DinA5
Inhalte:
- Logo Grasbündel.de
- www. grasbündel.de
- Kunden bewerten mit 'sehr gut'
- Familienbetrieb seit über 100 Jahren
- Geprüftes Qualitätsheu aus der Eifel
- frischer, aromatischer Heuduft von naturbelassenen, grünen Eifelwiesen
- Heu, Stroh und viele weitere Produkte im Shop
- Ökologische Papier-Verpackung
- Schneller und kostengünstiger Versand
Zusatzinfos:
- Die Datei normalheupng.png kann als Logo verwendet werden
- Als Idee könnte evt. auch ein Bild 89328394.jpg (Eifellandschaft Heuernte) in irgendweiner Form integriert werden.
- Folgende Bilddateien wurden über Bildaro gekauft:
- Es können bei Bedarf auch Kosten für weitere Bilder erworben werden

```html
<!DOCTYPE html>
<html lang="de">
<head>
<meta charset="utf-8">
<title>Grasbündel – Heulieferant Flyer</title>
<link href="https://fonts.googleapis.com/css2?family=Lato:wght@400;700&family=Zilla+Slab:wght@500;700&display=swap" rel="stylesheet">
<style>
  :root{
    --page:#eeeeee;
    --white:#ffffff;
    --green:#6fb23b;
    --green-dark:#5c9a2c;
    --blue:#0b608f;
    --orange:#f08a1c;
    --navy:#173a5e;
    --ink:#1c1c1c;
  }
  *{box-sizing:border-box;margin:0;padding:0}
  html,body{width:1200px;height:811px;overflow:hidden;background:var(--page)}
  body{font-family:"Lato",sans-serif;position:relative}
  .flyer{position:absolute;left:63px;top:135px;width:1079px;height:540px;background:var(--white);box-shadow:0 2px 6px rgba(0,0,0,.12);overflow:hidden}
  .header{position:absolute;left:0;top:0;width:100%;height:111px;background:var(--white)}
  .rating-badge{position:absolute;left:39px;top:18px;width:80px;height:78px;border:2px solid #d9d9d9;border-radius:4px;background:#f6f6f6}
  .rating-badge .stars-bar{position:absolute;left:8px;top:30px;width:60px;height:10px;background:#f2c230;border-radius:2px}
  .rating-badge .score-bar{position:absolute;left:8px;top:48px;width:60px;height:8px;background:#cfcfcf;border-radius:2px}
  .rating-arrow{position:absolute;left:133px;top:24px}
  .rating-text{position:absolute;left:134px;top:64px;font-size:14.5px;line-height:18px;font-weight:700;color:var(--ink)}
  .contact{position:absolute;left:894px;top:24px;font-size:14.5px;line-height:18px;color:var(--navy)}
  .contact-icons{position:absolute;left:852px;top:24px}
  .hero{position:absolute;left:0;top:111px;width:100%;height:341px;background:linear-gradient(180deg,#8aa53a 0%,#b8b23a 30%,#c9b545 55%,#b9a83e 100%)}
  .hero-animals{position:absolute;right:0;top:0;width:460px;height:100%;background:radial-gradient(ellipse at 35% 60%,#8a8a4a 0%,#a39550 40%,rgba(200,170,120,0) 75%),radial-gradient(ellipse at 75% 55%,#e7d8c6 0%,rgba(230,210,190,0) 55%)}
  .logo{position:absolute;left:468px;top:48px;width:138px;height:138px;border-radius:50%;background:var(--white);display:flex;align-items:center;justify-content:center}
  .logo-name{font-family:"Lato",sans-serif;font-weight:700;font-size:20px;color:var(--ink)}
  .headline-box{position:absolute;left:0;top:244px;width:507px;height:86px;background:var(--green);display:flex;align-items:center;padding-left:32px}
  .headline{font-family:"Zilla Slab",serif;font-weight:700;font-size:70px;letter-spacing:1px;color:var(--white);line-height:1}
  .subline-box{position:absolute;left:0;top:337px;width:507px;height:43px;background:var(--green);display:flex;align-items:center;padding-left:34px}
  .subline{font-family:"Zilla Slab",serif;font-weight:500;font-size:20.5px;color:var(--white);letter-spacing:.2px}
  .shop-strip{position:absolute;left:627px;top:418px;width:452px;height:34px;background:var(--green);display:flex;align-items:center;padding-left:38px;font-size:14.5px;color:var(--white)}
  .shop-strip strong{font-weight:700}
  .benefits{position:absolute;left:0;top:452px;width:100%;height:88px;background:var(--blue);border-top:3px solid var(--orange)}
  .benefit{position:absolute;top:0;height:85px;display:flex;align-items:center;gap:14px;color:var(--white);font-size:14.5px;line-height:18px;font-weight:700}
  .benefit svg{flex:none}
</style>
</head>
<body>
<div class="flyer">
  <header class="header">
    <div class="rating-badge"><div class="stars-bar"></div><div class="score-bar"></div></div>
    <svg class="rating-arrow" width="44" height="30" viewBox="0 0 44 30" fill="none" stroke="#1c1c1c" stroke-width="1.6" stroke-linecap="round">
      <path d="M40 26 C34 12 22 6 6 8"/><path d="M12 3 L5 8 L12 13"/>
    </svg>
    <p class="rating-text">Kunden bewerten<br>mit „sehr gut“</p>
    <svg class="contact-icons" width="30" height="70" viewBox="0 0 30 70" fill="none" stroke="#173a5e" stroke-width="1.6">
      <path d="M15 26 C8 18 6 14 6 10 a9 9 0 0 1 18 0 c0 4-2 8-9 16z"/><circle cx="15" cy="10" r="3.5"/>
      <ellipse cx="15" cy="27" rx="12" ry="3"/>
      <rect x="3" y="50" width="24" height="16" rx="1"/><path d="M3 50 L15 60 L27 50"/>
      <path d="M15 47 c-2-3-6-2-5 1 c1 2 5 4 5 4 s4-2 5-4 c1-3-3-4-5-1z"/>
    </svg>
    <p class="contact">Inhaber: M. Brandt<br>Lindenweg 12<br>53547 Talhausen<br>mail@grasbuendel.de</p>
  </header>

  <section class="hero" role="img" aria-label="Foto: Eifelwiese mit Heuballen, großer Heuballen mit Kaninchen und Meerschweinchen">
    <div class="hero-animals"></div>
  </section>

  <div class="logo"><span class="logo-name">Grasbündel</span></div>

  <div class="headline-box"><h1 class="headline">HEULIEFERANT</h1></div>
  <div class="subline-box"><p class="subline">FÜR KANINCHEN, NAGER UND DEN KLEINTIERBEDARF</p></div>

  <div class="shop-strip"><span>Heu, Stroh und vieles mehr im Shop:&nbsp;<strong>www.grasbuendel.de</strong></span></div>

  <footer class="benefits">
    <div class="benefit" style="left:42px">
      <svg width="56" height="50" viewBox="0 0 56 50" fill="none" stroke="#fff" stroke-width="3" stroke-linejoin="round">
        <rect x="8" y="20" width="36" height="26"/><path d="M4 14 L50 10 L51 20 L5 24z"/><path d="M8 36 L44 24"/>
        <path d="M26 12 c-4-8-12-8-10-2 c1 3 6 3 10 2 c4-2 10-8 4-9 c-4 0-4 5-4 9"/>
      </svg>
      <span>Ökologische<br>Papier-Verpackung</span>
    </div>
    <div class="benefit" style="left:290px">
      <svg width="64" height="44" viewBox="0 0 64 44" fill="none" stroke="#fff" stroke-width="3" stroke-linejoin="round">
        <path d="M16 6 H46 V32 H16"/><path d="M46 14 H55 L62 22 V32 H46"/>
        <circle cx="24" cy="34" r="5"/><circle cx="52" cy="34" r="5"/>
        <path d="M2 12 H12 M6 18 H14 M2 24 H12"/>
      </svg>
      <span>Schneller und kosten-<br>günstiger Versand</span>
    </div>
    <div class="benefit" style="left:570px">
      <svg width="66" height="50" viewBox="0 0 66 50" fill="none" stroke="#fff" stroke-width="3" stroke-linejoin="round">
        <path d="M4 24 L33 3 L62 24"/><path d="M12 19 V46 H54 V19"/><path d="M27 46 V30 H39 V46"/><path d="M20 8 V14"/><path d="M2 47 H64"/>
      </svg>
      <span>Familienbetrieb seit<br>über 100 Jahren</span>
    </div>
    <div class="benefit" style="left:830px">
      <svg width="50" height="62" viewBox="0 0 50 62" fill="none" stroke="#fff" stroke-width="3" stroke-linejoin="round">
        <circle cx="25" cy="22" r="19"/><circle cx="25" cy="22" r="13"/>
        <path d="M25 14 l2.5 5 5.5 .8 -4 3.8 1 5.4 -5-2.6 -5 2.6 1-5.4 -4-3.8 5.5-.8z"/>
        <path d="M16 39 V58 L25 52 L34 58 V39"/>
      </svg>
      <span>Geprüftes Qualitätsheu<br>aus der Eifel</span>
    </div>
  </footer>
</div>
</body>
</html>
```